Artificial Intelligence based service LanePilot.ai

Looking for a website for service designed for driving schools to deliver AI based solutions and features. File are to include various pages from contact to list of services to faqs, demos and more. we are looking for a website for AI based service for driving schools. services will include things like chat bots, voice agent, document processing and ai based marketing.

Target Market(s)

driving school owners and managers.

Industry/Entity Type

software and AI

Number of Pages Required

4 page

Font styles to use
Sans Serif

Requirements
Must have
• clean and easy to navigate pages. responsive. also delivery via FIGMA.

```html
<!DOCTYPE html>
<html lang="en">
<head>
<meta charset="utf-8">
<title>LanePilot.ai — 24/7 Voice Agent for Driving Schools</title>
<link href="https://fonts.googleapis.com/css2?family=Michroma&family=Poppins:wght@400;500;600&display=swap" rel="stylesheet">
<style>
:root{
  --green:#5cb85a;
  --green-soft:#dcefd9;
  --navy:#1b3e6c;
  --navy-deep:#122c52;
  --ink:#1d1d1f;
  --muted:#4a4f57;
  --card:#e4edf5;
  --icon-bg:#d6e3ec;
  --white:#ffffff;
  --star:#f5c518;
}
*{box-sizing:border-box;margin:0;padding:0}
html,body{width:1200px;height:3659px;overflow:hidden}
body{position:relative;font-family:"Poppins",sans-serif;color:var(--ink);background:var(--white)}
.display{font-family:"Michroma",sans-serif;font-weight:400;letter-spacing:.5px}
.abs{position:absolute}
.btn{position:absolute;display:flex;align-items:center;justify-content:center;background:var(--green);color:var(--white);font-size:14px;border-radius:3px;font-weight:500}

/* hero */
.hero{position:absolute;left:0;top:0;width:1200px;height:672px;background:radial-gradient(ellipse at 55% 55%,#5a5f66 0%,#34383e 45%,#15181c 100%)}
.brand{position:absolute;left:121px;top:30px;color:var(--white);font-size:19px;font-weight:600;display:flex;align-items:center;gap:8px}
.brand .dot{width:12px;height:12px;background:var(--green)}
.nav{position:absolute;top:34px;left:596px;display:flex;gap:30px;font-size:12px;color:var(--white)}
.nav .active{color:var(--green)}
.hero h1{position:absolute;top:185px;width:1200px;text-align:center;color:var(--white);font-size:44px;line-height:54px}
.hero h1 span{color:var(--green)}
.checks{position:absolute;top:305px;width:1200px;display:flex;justify-content:center;gap:52px;color:var(--white);font-size:15px}
.checks div{display:flex;align-items:center;gap:6px}

/* questions */
.q-title{position:absolute;top:717px;width:1200px;text-align:center;font-size:33px;line-height:43px}
.q-item{position:absolute;top:842px;width:240px;text-align:center}
.q-icon{width:97px;height:82px;margin:0 auto;background:#e6ecef;border-radius:10px;display:flex;align-items:center;justify-content:center}
.q-item p{margin-top:28px;font-size:22px;font-weight:500}
.result-pill{position:absolute;left:304px;top:994px;width:591px;height:26px;background:var(--green-soft);border-radius:13px;font-size:12px;display:flex;align-items:center;justify-content:center}

/* why band */
.why{position:absolute;left:0;top:1077px;width:1200px;height:447px;background:linear-gradient(90deg,var(--navy-deep) 0%,var(--navy) 40%,#3d6a8f 70%,#6a8aa0 100%)}
.why h2{position:absolute;left:121px;top:103px;color:var(--white);font-size:32px;line-height:42px}
.why p{position:absolute;left:121px;top:194px;width:440px;color:var(--white);font-size:11.5px;line-height:17px}

/* cards */
.card{position:absolute;background:var(--card);border-radius:14px;padding:0 18px}
.card.dark{background:linear-gradient(160deg,#4b6688,#2e4a6f)}
.card-icon{position:absolute;left:18px;top:18px;width:84px;height:72px;background:var(--icon-bg);border-radius:8px;display:flex;align-items:center;justify-content:center}
.card h3{position:absolute;left:18px;top:104px;font-size:22px;font-weight:500}
.card .desc{position:absolute;left:18px;top:143px;width:260px;font-size:11.5px;line-height:15px;color:var(--muted)}
.card .res{position:absolute;left:18px;top:184px;width:260px;font-size:11.5px;line-height:15px;font-weight:600}
.card.dark h3,.card.dark .desc,.card.dark .res{color:var(--white)}
.card.dark .card-icon{background:transparent}

/* benefits */
.benefits{position:absolute;left:0;top:2149px;width:1200px;height:628px;background:var(--navy)}
.benefits h2{position:absolute;top:50px;width:1200px;text-align:center;color:var(--white);font-size:33px}
.ben-photo{position:absolute;left:122px;top:131px;width:445px;height:436px;border-radius:16px;background:linear-gradient(135deg,#c9ccd2,#8c8f97 50%,#4c4f57)}
.ben-item{position:absolute;left:630px;display:flex;align-items:center;gap:14px;color:var(--white);font-size:17px;font-weight:500}

/* testimonials */
.t-title{position:absolute;top:2845px;width:1200px;text-align:center;font-size:33px}
.avatar{position:absolute;left:556px;top:2903px;width:88px;height:88px;border-radius:50%;border:2px solid var(--navy);background:linear-gradient(#bfe0e3,#7fb7bf)}
.t-name{position:absolute;top:3008px;width:1200px;text-align:center;font-size:13px;color:var(--muted)}
.t-quote{position:absolute;top:3047px;width:1200px;text-align:center;font-size:18px;line-height:23px}
.stars{position:absolute;top:3102px;width:1200px;text-align:center;color:var(--star);font-size:15px;letter-spacing:1px}

/* cta */
.cta{position:absolute;left:0;top:3176px;width:1200px;height:297px;background:var(--green)}
.cta h2{position:absolute;top:42px;width:1200px;text-align:center;color:var(--white);font-size:32px;line-height:41px}
.cta .b{position:absolute;top:186px;height:47px;border-radius:3px;display:flex;align-items:center;justify-content:center;font-size:15px;font-weight:500}
.cta .b.navy{background:var(--navy);color:var(--white)}
.cta .b.light{background:var(--white);color:var(--ink)}

/* footer */
.footer{position:absolute;left:0;top:3473px;width:1200px;height:186px;background:var(--navy);color:var(--white)}
.f-links{position:absolute;left:121px;top:79px;display:flex;gap:18px;font-size:11px;font-weight:500}
.f-copy{position:absolute;left:121px;top:103px;font-size:9.5px}
.f-brand{position:absolute;left:511px;top:68px;width:178px;text-align:center;font-size:22px;font-weight:600}
.f-news{position:absolute;left:862px;top:66px;font-size:13px}
.f-input{position:absolute;left:862px;top:91px;width:215px;height:30px;border:1px solid #5d79a0;border-radius:3px;display:flex}
.f-input span{flex:1;padding-left:12px;font-size:11px;line-height:28px}
.f-input b{width:76px;background:var(--green);font-size:11px;font-weight:500;display:flex;align-items:center;justify-content:center}
</style>
</head>
<body>

<header class="hero" role="img" aria-label="Photo of a driver's hands on a steering wheel inside a car">
  <div class="brand"><span class="dot"></span>LanePilot.ai</div>
  <nav class="nav"><span class="active">Home</span><span>About Us</span><span>Why Driving Schools</span><span>Real Benefits</span></nav>
  <div class="btn" style="left:980px;top:26px;width:97px;height:32px;font-size:12px">Contact Us</div>
  <h1 class="display">Boost Your <span>Driving School</span><br>with a 24/7 Voice Agent</h1>
  <div class="checks">
    <div><svg width="18" height="18" viewBox="0 0 18 18"><circle cx="9" cy="9" r="9" fill="#5cb85a"/><path d="M5 9l3 3 5-6" stroke="#fff" stroke-width="2" fill="none"/></svg>Automate Calls</div>
    <div><svg width="18" height="18" viewBox="0 0 18 18"><circle cx="9" cy="9" r="9" fill="#5cb85a"/><path d="M5 9l3 3 5-6" stroke="#fff" stroke-width="2" fill="none"/></svg>Answer Questions Instantly</div>
    <div><svg width="18" height="18" viewBox="0 0 18 18"><circle cx="9" cy="9" r="9" fill="#5cb85a"/><path d="M5 9l3 3 5-6" stroke="#fff" stroke-width="2" fill="none"/></svg>Never Miss a Student Again.</div>
  </div>
  <div class="btn" style="left:530px;top:359px;width:139px;height:49px">Learn More</div>
</header>

<section>
  <h2 class="q-title display">High Call Volume &amp;<br>Repetitive Questions</h2>
  <div class="q-item" style="left:50px"><div class="q-icon"><svg width="48" height="48" viewBox="0 0 48 48" fill="none" stroke="#5cb85a" stroke-width="2"><path d="M10 4h20l8 8v30H10z"/><path d="M16 16h14M16 22h10M16 28h8"/><circle cx="32" cy="34" r="7"/><path d="M32 30v8"/></svg></div><p>Pricing</p></div>
  <div class="q-item" style="left:324px"><div class="q-icon"><svg width="48" height="48" viewBox="0 0 48 48" fill="none" stroke="#5cb85a" stroke-width="2"><rect x="10" y="6" width="28" height="36" rx="2"/><rect x="16" y="12" width="16" height="20"/><path d="M20 24h8M22 20h4"/></svg></div><p>Permit requirements</p></div>
  <div class="q-item" style="left:597px"><div class="q-icon"><svg width="48" height="48" viewBox="0 0 48 48" fill="none" stroke="#5cb85a" stroke-width="2"><rect x="8" y="8" width="32" height="24"/><path d="M24 32v8M16 42h16M14 16h20M14 22h12"/></svg></div><p>Class availability</p></div>
  <div class="q-item" style="left:871px"><div class="q-icon"><svg width="48" height="48" viewBox="0 0 48 48" fill="none" stroke="#5cb85a" stroke-width="2"><path d="M10 6h22v14M10 6v34h14"/><path d="M15 14h12M15 20h10M15 26h6"/><path d="M26 38v-6l3-5h10l3 5v6z"/><circle cx="30" cy="38" r="2"/><circle cx="38" cy="38" r="2"/></svg></div><p>Road test steps</p></div>
  <div class="result-pill"><b style="font-weight:600">Result:</b>&nbsp;Less time answering the same questions, more time delivering great lessons.</div>
</section>

<section class="why" role="img" aria-label="Photo of a driver using a dashboard touchscreen on a mountain road">
  <h2 class="display">Why Driving Schools<br>Choose Voice Agents</h2>
  <p>Running a driving school means juggling lesson schedules, student questions, staff changes, and constant phone calls. A Voice Agent is your AI-powered assistant that answers the phone 24/7, handles routine questions, and gives your staff room to breathe—without the cost of hiring more people.</p>
  <div class="btn" style="left:121px;top:289px;width:140px;height:49px">Learn More</div>
</section>

<section>
  <div class="card" style="left:122px;top:1577px;width:304px;height:244px">
    <div class="card-icon"><svg width="44" height="44" viewBox="0 0 44 44" fill="none" stroke="#5cb85a" stroke-width="2"><path d="M36 22a14 14 0 1 1-5-10.7"/><path d="M32 6v6h-6"/><text x="10" y="27" font-size="11" fill="#5cb85a" stroke="none" font-family="Poppins">24/7</text></svg></div>
    <h3>After-Hours Availability</h3>
    <p class="desc">Missed calls = missed business. Your voice agent works evenings, weekends, and holidays.</p>
    <p class="res">Result: Convert more inquiries into paying students—even while you sleep.</p>
  </div>
  <div class="card dark" style="left:447px;top:1577px;width:304px;height:244px" role="img" aria-label="Photo of an office staff member at a front desk">
    <div class="card-icon"><svg width="44" height="44" viewBox="0 0 44 44" fill="none" stroke="#5cb85a" stroke-width="2"><circle cx="22" cy="22" r="14" stroke-dasharray="4 3"/><circle cx="22" cy="19" r="4"/><path d="M15 29c2-4 12-4 14 0"/></svg></div>
    <h3>Admin Staff Turnover</h3>
    <p class="desc">Hiring and training office staff takes time. A voice agent is ready on day one.</p>
    <p class="res">Result: Consistent, professional service—no matter who's at the front desk.</p>
  </div>
  <div class="card" style="left:771px;top:1577px;width:306px;height:244px">
    <div class="card-icon"><svg width="44" height="44" viewBox="0 0 44 44" fill="none" stroke="#5cb85a" stroke-width="2"><circle cx="12" cy="12" r="5"/><circle cx="32" cy="32" r="5"/><path d="M18 10c8 0 14 4 14 16M26 34c-8 0-14-4-14-16"/></svg></div>
    <h3>Language Barriers</h3>
    <p class="desc">Serve more students with support for multiple languages.</p>
    <p class="res" style="top:184px">Result: Improve access and satisfaction for non-English-speaking families.</p>
  </div>
  <div class="card" style="left:122px;top:1841px;width:467px;height:243px">
    <div class="card-icon" style="top:18px"><svg width="44" height="44" viewBox="0 0 44 44" fill="none" stroke="#5cb85a" stroke-width="2"><circle cx="22" cy="22" r="15"/><circle cx="22" cy="19" r="5"/><path d="M13 32c3-6 15-6 18 0"/></svg></div>
    <h3 style="top:102px">Instructor Absences &amp; Rescheduling</h3>
    <p class="desc" style="width:380px;top:140px">Integrated with your booking system, your voice agent can help reschedule or notify students of changes.</p>
    <p class="res" style="width:400px;top:183px">Result: Fewer cancellations and smoother communication</p>
  </div>
  <div class="card" style="left:609px;top:1841px;width:468px;height:243px">
    <div class="card-icon"><svg width="44" height="44" viewBox="0 0 44 44" fill="none" stroke="#5cb85a" stroke-width="2"><path d="M34 14a15 15 0 1 0 2 12"/><path d="M36 8v7h-7"/><path d="M26 16c-2-2-8-2-8 2s8 2 8 6-6 4-8 2M22 12v20"/></svg></div>
    <h3 style="top:102px">No Expensive Tech Investment</h3>
    <p class="desc" style="width:400px;top:140px">Voice agents run in the cloud and integrate with your existing phone system.</p>
    <p class="res" style="width:400px;top:183px">Result: No hardware, low setup costs, and immediate ROI.</p>
  </div>
</section>

<section class="benefits">
  <h2 class="display">Real Benefits for Your School</h2>
  <div class="ben-photo" role="img" aria-label="Photo of a happy new driver holding car keys in a car doorway"></div>
  <div class="ben-item" style="top:147px"><svg width="44" height="44" viewBox="0 0 44 44" fill="none" stroke="#5cb85a" stroke-width="2"><circle cx="22" cy="22" r="15"/><path d="M8 22a14 14 0 0 1 28 0"/><rect x="5" y="20" width="5" height="9"/><rect x="34" y="20" width="5" height="9"/></svg><span>24/7 live call support—no more missed calls</span></div>
  <div class="ben-item" style="top:222px"><svg width="44" height="44" viewBox="0 0 44 44" fill="none" stroke="#5cb85a" stroke-width="2"><circle cx="24" cy="24" r="13"/><path d="M24 16v8l5 4M2 20h8M4 26h6M6 32h6"/></svg><span>Faster response times = happier customers</span></div>
  <div class="ben-item" style="top:293px"><svg width="44" height="44" viewBox="0 0 44 44" fill="none" stroke="#5cb85a" stroke-width="2"><circle cx="22" cy="22" r="6"/><path d="M22 6v6M22 32v6M6 22h6M32 22h6M10 10l4 4M30 30l4 4M10 34l4-4M30 14l4-4"/></svg><span>Less admin stress for you and your team</span></div>
  <div class="ben-item" style="top:364px"><svg width="44" height="44" viewBox="0 0 44 44" fill="none" stroke="#5cb85a" stroke-width="2"><circle cx="22" cy="22" r="15"/><rect x="13" y="16" width="18" height="12"/><circle cx="19" cy="22" r="2"/><path d="M24 20h5M24 24h4"/></svg><span>Lower operating costs than live staff</span></div>
  <div class="ben-item" style="top:440px"><svg width="44" height="44" viewBox="0 0 44 44" fill="none" stroke="#5cb85a" stroke-width="2"><circle cx="22" cy="22" r="15"/><rect x="14" y="14" width="16" height="16"/><path d="M14 20h16M19 14v16"/></svg><span>More bookings, fewer no-shows</span></div>
  <div class="ben-item" style="top:501px"><svg width="44" height="44" viewBox="0 0 44 44" fill="none" stroke="#5cb85a" stroke-width="2"><circle cx="20" cy="24" r="13"/><circle cx="20" cy="24" r="5"/><circle cx="32" cy="12" r="6"/><path d="M29 12l2 2 4-4"/></svg><span>A modern, professional image</span></div>
</section>

<section>
  <h2 class="t-title display">Clients Testimonials</h2>
  <svg class="abs" style="left:103px;top:2973px" width="16" height="24" viewBox="0 0 16 24"><path d="M12 2L3 12l9 10" stroke="#1b3e6c" stroke-width="2" fill="none"/></svg>
  <svg class="abs" style="left:1046px;top:2973px" width="16" height="24" viewBox="0 0 16 24"><path d="M4 2l9 10-9 10" stroke="#1b3e6c" stroke-width="2" fill="none"/></svg>
  <div class="avatar" role="img" aria-label="Client portrait photo"></div>
  <p class="t-name">Dana Whitfield</p>
  <p class="t-quote">"Since adding a voice agent, we've cut our call<br>volume in half—and enrollment is up!"</p>
  <p class="stars">★★★★★</p>
</section>

<section class="cta">
  <h2 class="display">Ready to Automate Your Front<br>Desk? Let your school sound smarter,<br>faster, and more helpful—24 hours a day.</h2>
  <div class="b navy" style="left:295px;width:172px">Book a Free Demo</div>
  <div class="b light" style="left:480px;width:240px">Specialist Talk to a Product</div>
  <div class="b navy" style="left:733px;width:172px">See It in Action</div>
</section>

<footer class="footer">
  <div class="f-links"><span>About Us</span><span>Why Driving Schools</span><span>Real Benefits</span></div>
  <div class="f-copy">© 2025 LANEPILOT.AI</div>
  <div class="f-brand">LanePilot.ai</div>
  <div class="f-news">Newsletter Signup</div>
  <div class="f-input"><span>Email</span><b>Subscribe</b></div>
</footer>

</body>
</html>
```